Redesign of existing website for a corporate advisory business focussed on technology

We need a redesign of our website. We are a corporate advisory business based in Sydney. Our focus is on the technology and life-science sectors. We assist our clients with capital raisings, mergers and acquisitions and other corporate transactions.

Our business is called "Harbour Ridge Partners"
Our current website is www.harbourridgeadv.com.au

I'd like to see a complete re-design of the site. (I'm happy to keep any of the existing images - but equally happy to scrap them completely and "start again".)

My preference is that the logo remain as it is. However, I would be very open to a re-colouring of the logo if it works better with a new webiste design.

The content of the website will remain the same. I'd like one additional section - "News" - which will allow us to manually post news items and which will pull in news feeds from current and past clients.

In terms of positioning / look-and-feel:

Our clients fall into two categories. I'd like the website to appeal to both:

1. The first category is: Executives from established technology or life-science companies (private or public), who engage us to assist with strategy, capital raising, corporate transactions.

2. The second category is: Entrepreneurs looking for advice in accessing angel funding or venture capital. The site should appeal to young tech-savvy entrepreneurs who are looking to engage a firm to provide such assistance.

To accomodate both target groups, the overriding feel should be one of professionalism, stability, trust and expertise. However, while the site should look fairly "corporate", I'd like it to feel contemporary and have an element of creativity and flair, reflecting the fact that our clients are often early-stage, innovative, technology companies. (I know this might be a tricky balance...)

Target Market(s)

Potential clients. Typically executives at technology or life-science companies or (more typically) entrepreneurs building their own companies

Industry/Entity Type

Business

Requirements
Must have
• 1. All content on the existing website
2. An additional section called "News" that allows us to easily add news items or articles and ideally which accepts news feeds from a handful of past and present clients
3. An ability to easily update and edit content
Should not have
• The site should not have "gimmicks". (Definitely no devices like the moving arrow in the current site!)

It should be fairly conservative, while still feeling contemporary and fresh.

```html
<!DOCTYPE html>
<html lang="en">
<head>
<meta charset="utf-8">
<title>Harbour Ridge Partners</title>
<link rel="stylesheet" href="https://fonts.googleapis.com/css2?family=Ubuntu:wght@300;400;500;700&family=Arimo:ital,wght@0,400;0,700;1,700&display=swap">
<style>
:root{
  --orange:#f26a2c;
  --orange-deep:#e2561c;
  --orange-light:#ff8a44;
  --ink:#2b2b2b;
  --grey-text:#444;
  --navy:#222a35;
  --navy-2:#2e3642;
  --navy-3:#3a4350;
  --white:#fff;
  --rule:#d9d9d9;
  --soft:#f3f3f3;
}
*{margin:0;padding:0;box-sizing:border-box}
html,body{width:1169px;height:1200px;overflow:hidden;background:var(--white)}
body{position:relative;font-family:'Arimo',Arial,sans-serif;color:var(--ink)}
.abs{position:absolute}

/* header */
.brand{left:126px;top:11px;display:flex;align-items:center;gap:14px}
.brand-dot{width:85px;height:85px;border-radius:50%;background:var(--orange)}
.brand-name{font-family:'Ubuntu',sans-serif;font-weight:400;font-size:29px;color:var(--ink);letter-spacing:.2px}
.connect{left:727px;top:52px;display:flex;align-items:center;gap:12px;font-family:'Ubuntu',sans-serif;font-weight:500;font-size:19px;color:#444}
.social{display:flex;gap:12px;margin-left:10px}
.social span{width:25px;height:25px;border-radius:4px;background:#5b8fb9}
.social span:nth-child(2){background:#1c6fa3}
.social span:nth-child(3){background:#3f62a8}

/* hero */
.hero{left:0;top:135px;width:1169px;height:368px;background:radial-gradient(ellipse at 40% 45%,#ff9c5c 0%,var(--orange) 55%,var(--orange-deep) 100%)}
.nav{left:119px;top:116px;width:915px;height:47px;border-radius:14px;background:linear-gradient(#5a5a5a,#2a2a2a 55%,#1a1a1a);display:flex;font-family:'Ubuntu',sans-serif;font-weight:500;font-size:13px;color:var(--white)}
.nav a{color:inherit;text-decoration:none;display:flex;align-items:center;justify-content:center;height:100%;border-left:1px solid #111;box-shadow:inset 1px 0 0 #555}
.nav .home{margin-left:54px;width:92px;background:linear-gradient(var(--orange-light),var(--orange-deep));border:0;box-shadow:none;position:relative}
.nav .home::before{content:"";position:absolute;left:0;top:-8px;width:100%;height:8px;background:var(--orange)}
.nav .w1{width:152px}.nav .w2{width:119px}.nav .w3{width:151px}.nav .w4{width:110px;border-left:1px solid #111}
.hero-title{left:125px;top:196px;font-family:'Ubuntu',sans-serif;color:var(--white);line-height:36px}
.hero-title .light{font-weight:300;font-size:31px}
.hero-title .bold{font-weight:700;font-size:30px;letter-spacing:.8px;display:block}
.hero-title .dark{color:#222}
.hero-copy{left:126px;top:327px;width:414px;font-size:12.5px;line-height:18px;color:var(--white);text-align:justify}
.hero-copy em{font-weight:700}
.read-btn{left:124px;top:445px;width:132px;height:36px;border:2px solid #fff;border-radius:18px;background:linear-gradient(var(--orange-light),var(--orange-deep));color:var(--white);font-family:'Ubuntu',sans-serif;font-size:14px;display:flex;align-items:center;justify-content:center}
.hero-photo{left:605px;top:170px;width:435px;height:333px;background:linear-gradient(180deg,#b9724a 0%,#4a3a34 55%,#2c2624 100%);border-radius:120px 120px 0 0;opacity:.9}

/* feature band */
.band{left:0;top:503px;width:1169px;height:180px;background:linear-gradient(var(--navy-3),var(--navy));border-top:2px solid #fff}
.feature{top:523px;width:300px;color:var(--white)}
.feature .dot{position:absolute;left:0;top:2px;width:42px;height:42px;border-radius:50%;background:var(--orange);border:2px solid #ffb58a}
.feature h3{margin-left:55px;font-family:'Ubuntu',sans-serif;font-weight:500;font-size:19px}
.feature .sub{margin-left:55px;font-family:'Ubuntu',sans-serif;font-size:13px;color:var(--orange-light);font-weight:500;letter-spacing:.4px;margin-top:2px}
.feature p{margin:26px 0 0 6px;font-family:'Ubuntu',sans-serif;font-weight:500;font-size:11.2px;line-height:18px}
.feature .more{margin:12px 0 0 6px;display:flex;align-items:center;gap:8px;font-family:'Ubuntu',sans-serif;font-size:12px;text-decoration:underline}
.feature .more i{width:14px;height:14px;border-radius:50%;background:#ddd;display:inline-block;position:relative}
.feature .more i::after{content:"";position:absolute;left:5px;top:3.5px;border-left:5px solid #333;border-top:3.5px solid transparent;border-bottom:3.5px solid transparent}
.vrule{top:523px;width:1px;height:150px;background:#1a2029;box-shadow:1px 0 0 #46505c}

/* intro */
.intro-title{left:95px;top:707px;font-family:'Ubuntu',sans-serif;font-size:19px;color:var(--orange-deep)}
.intro-title span{color:var(--ink)}
.intro-photo{left:93px;top:752px;width:200px;height:146px;background:linear-gradient(180deg,#dfe6ef 0%,#9fb2c7 55%,#3b4a5e 100%)}
.intro-shadow{left:80px;top:898px;width:222px;height:16px;background:radial-gradient(ellipse at 50% 0,rgba(0,0,0,.35),transparent 70%)}
.intro-copy{left:308px;top:761px;width:415px;font-size:11.5px;line-height:18px;letter-spacing:.6px;color:var(--grey-text);text-align:justify}
.intro-copy p+p{margin-top:18px}
.intro-copy b{color:#333}
.view-more{font-size:12px;color:var(--orange-deep)}

/* articles */
.articles{left:781px;top:709px;width:268px;height:208px;border:1px solid var(--rule);border-radius:6px;background:linear-gradient(#fff,#ececec);box-shadow:0 2px 3px rgba(0,0,0,.15)}
.articles-tab{left:775px;top:728px;width:228px;height:31px;border-radius:4px 8px 8px 0;background:linear-gradient(var(--orange-light),var(--orange-deep));font-family:'Ubuntu',sans-serif;font-weight:500;font-size:18px;color:var(--white);padding:4px 0 0 25px}
.article{left:795px;width:245px;display:flex;gap:10px}
.avatar{width:43px;height:36px;border:3px solid #fff;box-shadow:0 0 2px #888;background:linear-gradient(#cfd6dd,#7d8a96)}
.article .txt{font-size:12px;line-height:18px;letter-spacing:.5px;color:#333}
.article .txt b{font-weight:400;font-size:12.5px}
.article .meta{color:#555}

.sep{left:0;top:935px;width:1169px;height:15px;background:linear-gradient(#e6e6e6,#cfd2d6)}

/* footer */
.footer{left:0;top:950px;width:1169px;height:187px;background:linear-gradient(var(--navy-2),var(--navy))}
.foot-h{font-family:'Ubuntu',sans-serif;font-weight:500;font-size:18px;color:var(--white);display:flex;align-items:center;gap:10px}
.links{left:104px;top:1005px;list-style:none;font-family:'Ubuntu',sans-serif;font-size:14px;color:#e8e8e8}
.links li{display:flex;align-items:center;gap:10px;height:30px}
.testi-logo{left:335px;top:1002px;width:130px;height:76px;background:#111;padding:4px}
.testi-logo div{width:100%;height:100%;background:#fff;display:flex;align-items:center;justify-content:center;font-family:'Ubuntu',sans-serif;font-weight:500;font-size:19px;color:#7a5a12}
.testi-side{left:476px;top:1002px;width:242px;font-family:'Ubuntu',sans-serif;font-size:12.5px;line-height:18px;color:#ddd}
.testi-side span{color:var(--orange)}
.testi-foot{left:340px;top:1084px;width:385px;font-family:'Ubuntu',sans-serif;font-size:12.5px;line-height:18px;color:#ddd}
.pager{left:654px;top:1119px;display:flex;gap:11px}
.pager i{width:8px;height:7px;background:#ccc}
.pager i:first-child{background:var(--orange)}
.contact{left:840px;top:1000px;font-family:'Ubuntu',sans-serif;font-size:12.5px;line-height:18px;color:#e6e6e6}
.contact .k{color:var(--orange)}
.frule{top:970px;width:1px;height:150px;background:#1a2029;box-shadow:1px 0 0 #3e4753}
.bottom{left:0;top:1137px;width:1169px;height:63px;background:linear-gradient(#3a424d,#1f252e);border-top:1px solid #4d5661;font-family:'Ubuntu',sans-serif;font-size:13px;color:#e6e6e6;display:flex;align-items:center;justify-content:center;padding-right:92px}
</style>
</head>
<body>

<header>
  <div class="abs brand"><span class="brand-dot"></span><span class="brand-name">harbour ridge partners</span></div>
  <div class="abs connect">Connect with us
    <svg width="24" height="20" viewBox="0 0 24 20"><path d="M2 10h18M12 2l9 8-9 8" fill="none" stroke="#f26a2c" stroke-width="3.5" stroke-linecap="round" stroke-linejoin="round"/></svg>
    <span class="social"><span></span><span></span><span></span></span>
  </div>
</header>

<section class="abs hero"></section>
<div class="abs hero-photo" role="img" aria-label="Photo of four smiling business people standing with arms folded"></div>
<nav class="abs nav">
  <a class="home">HOME</a><a class="w1">OUR SERVICES</a><a class="w2">OUR TEAM</a><a class="w3">OUR EXPERIENCE</a><a class="w4">CONTACT US</a>
</nav>
<h1 class="abs hero-title"><span class="light">A corporate advisory firm</span><span class="bold dark">with a focus on life-science</span><span class="bold">and technology !!</span></h1>
<p class="abs hero-copy"><em>Lorem ipsum dolor sit amet, consectetuer adipiscing elit. Nam nibh. Nunc varius facilisis eros.</em> Sed erat. In in velit quis arcu ornare laoreet. Curabitur adipiscing luctus massa. Integer ut purus ac augue commodo commodo. Nunc nec mi eu justo tempor consectetuer. Etiam vitae nisl.</p>
<div class="abs read-btn">READ MORE....</div>

<section class="abs band"></section>
<article class="abs feature" style="left:96px">
  <span class="dot"></span><h3>Our Team</h3><div class="sub">aeserunt mollitia animi</div>
  <p>We work with Australian life-science and technology companies providing independent corporate advice and disciplined transaction execution capabilities</p>
  <div class="more"><i></i>Read More</div>
</article>
<div class="abs vrule" style="left:407px"></div>
<article class="abs feature" style="left:434px">
  <span class="dot"></span><h3>Our Services</h3><div class="sub">aeserunt mollitia animi</div>
  <p>We work with Australian life-science and technology companies providing independent corporate advice and disciplined transaction execution capabilities</p>
  <div class="more"><i></i>Read More</div>
</article>
<div class="abs vrule" style="left:746px"></div>
<article class="abs feature" style="left:768px">
  <span class="dot"></span><h3>Our Experience</h3><div class="sub">aeserunt mollitia animi</div>
  <p>We work with Australian life-science and technology companies providing independent corporate advice and disciplined transaction execution capabilities</p>
  <div class="more"><i></i>Read More</div>
</article>

<h2 class="abs intro-title">A corporate advisory firm with a focus on <span>life-science and technology</span></h2>
<div class="abs intro-photo" role="img" aria-label="Silhouettes of business people in front of a pale world map"></div>
<div class="abs intro-shadow"></div>
<div class="abs intro-copy">
  <p><b>Harbour Ridge Partners is a specialist corporate advisory and investment firm with a focus on high growth companies in the Australian life-science</b> and technology sectors.Our team combines extensive investment banking and funds management experience with sector expertise and longstanding investor relationships.</p>
  <p>Our advisory work incorporates both equity capital markets as well as mergers and acquisitions Via our alliance</p>
  <div class="view-more" style="text-align:right;margin:3px 3px 0 0">View more [+]</div>
</div>

<aside>
  <div class="abs articles"></div>
  <div class="abs articles-tab">Latest Articles</div>
  <div class="abs article" style="top:774px"><span class="avatar" role="img" aria-label="Author portrait"></span><div class="txt"><b>Lorem Ipsum is simply dummy</b><br>text of the printing<br><span class="meta">May 15, 2012 // 4 Comments</span></div></div>
  <div class="abs article" style="top:835px"><span class="avatar" role="img" aria-label="Author portrait"></span><div class="txt"><b>Lorem Ipsum is simply dummy</b><br>text of the printing<br><span class="meta">May 15, 2012 // 4 Comments</span></div></div>
  <div class="abs view-more" style="left:951px;top:892px">View more [+]</div>
</aside>

<div class="abs sep"></div>
<footer class="abs footer"></footer>

<div class="abs foot-h" style="left:105px;top:965px">
  <svg width="24" height="24" viewBox="0 0 24 24"><rect x="1" y="1" width="22" height="22" fill="#fff" stroke="#999"/><rect x="4" y="4" width="16" height="16" fill="#f26a2c"/><path d="M8 16l7-7M10 9h5v5" stroke="#fff" stroke-width="2" fill="none"/></svg>All Links</div>
<ul class="abs links">
  <li><svg width="18" height="16" viewBox="0 0 18 16"><path d="M2 9l5 5L16 2" fill="none" stroke="#eee" stroke-width="3"/></svg>Home</li>
  <li><svg width="18" height="16" viewBox="0 0 18 16"><path d="M2 9l5 5L16 2" fill="none" stroke="#eee" stroke-width="3"/></svg>Our Services</li>
  <li><svg width="18" height="16" viewBox="0 0 18 16"><path d="M2 9l5 5L16 2" fill="none" stroke="#eee" stroke-width="3"/></svg>Our Team</li>
  <li><svg width="18" height="16" viewBox="0 0 18 16"><path d="M2 9l5 5L16 2" fill="none" stroke="#eee" stroke-width="3"/></svg>Our Experience</li>
</ul>
<div class="abs frule" style="left:276px"></div>

<div class="abs foot-h" style="left:339px;top:966px">
  <svg width="22" height="22" viewBox="0 0 22 22"><rect x="2" y="2" width="16" height="18" fill="#fff"/><path d="M5 7h10M5 11h10M5 15h7" stroke="#999"/><path d="M14 16l6-10" stroke="#f26a2c" stroke-width="2.5"/></svg>Client Testimonials</div>
<div class="abs testi-logo"><div>Northvale</div></div>
<p class="abs testi-side"><span>Lorem Ipsum is simply dummy text of the printing and typesetting</span> industry. Lorem Ipsum has been the industry's standard dummy text ever since the 1500s,</p>
<p class="abs testi-foot">Lorem Ipsum is simply dummy text of the printing and typesetting industry.</p>
<div class="abs pager"><i></i><i></i><i></i><i></i></div>
<div class="abs frule" style="left:777px"></div>

<div class="abs foot-h" style="left:822px;top:967px">
  <svg width="22" height="22" viewBox="0 0 22 22"><path d="M5 2l4 4-2.5 2.5c1 2.5 3.5 5 6 6L15 12l4 4-3 3C9 19 3 13 2 5z" fill="#f26a2c"/></svg>Contact Information</div>
<address class="abs contact" style="font-style:normal">
  Level 4, 18 Corran Lane<br>Pyrmont NSW 2009<br>Australia<br><br>
  <span class="k">Tel.</span> +61 2 9000 3172<br>
  <span class="k">Email.</span> info@harbourridgeadv.com.au<br>
  <span class="k">AFS License No:</span> 512907
</address>

<div class="abs bottom">Copyright @ Harbour Ridge Partners Pty Ltd 2011, AFS License No: 512907</div>

</body>
</html>
```